HARLOWE FREIGHT & PLANT HIRE NEEDS A FLYER

WE NEED A FLYER FOR OUR COMPANY <br/>WE SPECIALISE IN ROAD BUILDING AND MAINTENANCE, GENERAL EARTHWORK DAM REPAIRS & DESILTING, FENCE CLEARING, FIRE BREAKS, GRAVEL SOURCE AND DELIVERY GENERAL FREIGHT STEEL HAY LICK AND MCHINERY. <br/><br/>I HAVE UPLOAD A FILE THAT I LIKE AND WOULD LIKE SOMETHING THE SAME IF POSSIBLE. AND LOGO TO GO WITH IT.

```html
<!DOCTYPE html>
<html lang="en">
<head>
<meta charset="utf-8">
<title>Harlowe Freight &amp; Plant Hire Flyer</title>
<link href="https://fonts.googleapis.com/css2?family=Montserrat:ital,wght@0,800;1,800;1,900&family=Oswald:wght@500&display=swap" rel="stylesheet">
<style>
  :root {
    --page: #d9d9d9;
    --white: #ffffff;
    --orange: #f0a319;
    --orange-deep: #e0900f;
    --charcoal: #333333;
    --ink: #111111;
  }
  * { margin: 0; padding: 0; box-sizing: border-box; }
  html, body { width: 1200px; height: 1200px; overflow: hidden; background: var(--page); }
  .flyer {
    position: absolute; left: 180px; top: 56px;
    width: 840px; height: 1088px;
    background: var(--white); overflow: hidden;
    font-family: "Montserrat", Arial, sans-serif;
  }
  .flyer-shapes { position: absolute; inset: 0; }
  .tagline {
    position: absolute; right: 34px; top: 16px;
    color: var(--white); font-style: italic; font-weight: 900;
    font-size: 27px; line-height: 30px; text-align: right; letter-spacing: 0.5px;
  }
  .brand {
    position: absolute; left: 0; width: 840px; top: 160px;
    text-align: center; color: var(--charcoal); font-weight: 800;
  }
  .brand-name { font-size: 84px; line-height: 92px; letter-spacing: 2px; }
  .brand-line { font-size: 40px; line-height: 50px; }
  .brand-suffix { font-size: 30px; line-height: 40px; }
  .section { position: absolute; left: 28px; display: flex; flex-direction: column; }
  .section-title {
    color: var(--orange); font-style: italic; font-weight: 900;
    font-size: 29px; line-height: 36px; letter-spacing: 0.5px;
  }
  .section-rule {
    display: block; margin-left: -28px; margin-top: 4px; height: 5px;
    background: linear-gradient(90deg, #ffffff, #9a9a9a);
  }
  .section-list {
    list-style: none; margin-top: 9px;
    color: var(--white); font-style: italic; font-weight: 900;
    font-size: 20.5px; line-height: 33px; letter-spacing: 0.4px;
  }
  .dot { color: var(--orange); }
  .specialties { top: 412px; }
  .specialties .section-rule { width: 340px; }
  .machinery { top: 654px; }
  .machinery .section-rule { width: 663px; }
  .contact-names {
    position: absolute; right: 17px; top: 850px;
    font-family: "Oswald", "Arial Narrow", sans-serif; font-weight: 500;
    color: var(--white); font-size: 34px; line-height: 44px;
  }
  .phone-pill {
    position: absolute; left: 478px; top: 895px; width: 380px; height: 48px;
    background: var(--white); border-radius: 24px 0 0 24px;
  }
  .phone-icon { position: absolute; left: 12px; top: 6px; }
  .phone-number {
    position: absolute; right: 35px; top: 0;
    font-style: italic; font-weight: 900; font-size: 38px; line-height: 48px; color: var(--ink);
  }
  .email {
    position: absolute; right: 17px; top: 950px;
    color: var(--white); font-style: italic; font-weight: 900; font-size: 22px; line-height: 28px;
    display: flex; align-items: center; gap: 8px;
  }
</style>
</head>
<body>
<main class="flyer">
  <svg class="flyer-shapes" width="840" height="1088" viewBox="0 0 840 1088">
    <polygon points="0,0 840,0 840,93 368,93 323,35 0,35" fill="var(--orange)"/>
    <polygon points="0,275 840,512 840,1088 0,1088" fill="var(--charcoal)"/>
    <polygon points="493,393 840,480 840,512 493,422" fill="var(--orange)"/>
    <polygon points="0,1035 840,720 840,1088 0,1088" fill="var(--orange-deep)"/>
    <rect x="0" y="1040" width="840" height="48" fill="var(--charcoal)" role="img" aria-label="Mountain range silhouette along the bottom edge"/>
  </svg>

  <p class="tagline">FOR ALL YOUR FREIGHTS<br>AND PLANT HIRE NEEDS!</p>

  <div class="brand">
    <div class="brand-name">HARLOWE</div>
    <div class="brand-line">FREIGHT &amp; PLANT HIRE</div>
    <div class="brand-suffix">PTY LTD</div>
  </div>

  <section class="section specialties">
    <h2 class="section-title">SPECIALISING IN</h2>
    <span class="section-rule"></span>
    <ul class="section-list">
      <li>ROAD BUILDING AND MAINTENENCE <span class="dot">•</span></li>
      <li>GENERAL EARTHWORKS <span class="dot">•</span> DAM REPAIRS &amp; DESILTING <span class="dot">•</span></li>
      <li>FENCE CLEARING <span class="dot">•</span> FIRE BREAKS <span class="dot">•</span> GRAVEL SOURCE &nbsp;AND</li>
      <li>DELIVERY <span class="dot">•</span> GENERAL FREIGHT <span class="dot">•</span> STEEL <span class="dot">•</span> LICK <span class="dot">•</span> HAY <span class="dot">•</span></li>
      <li>MACHINERY <span class="dot">•</span></li>
    </ul>
  </section>

  <section class="section machinery">
    <h2 class="section-title">CURRENT MACHINERY AVAILABLE</h2>
    <span class="section-rule"></span>
    <ul class="section-list">
      <li>GRADER <span class="dot">•</span> LOADER &amp; STICK RACK <span class="dot">•</span> ROLLERS <span class="dot">•</span> DOZER <span class="dot">•</span></li>
      <li>WATER TRUCKS <span class="dot">•</span> SIDE TIPPERS <span class="dot">•</span> PRIME MOVERS <span class="dot">•</span></li>
      <li>FORKLIFT <span class="dot">•</span> SKID STEER LOADER <span class="dot">•</span></li>
      <li>FLAT TOPS <span class="dot">•</span> DROP DECK <span class="dot">•</span></li>
    </ul>
  </section>

  <p class="contact-names">GRANT &amp; MELISSA DORNE</p>

  <div class="phone-pill">
    <svg class="phone-icon" width="36" height="36" viewBox="0 0 36 36" aria-hidden="true">
      <circle cx="18" cy="18" r="18" fill="var(--charcoal)"/>
      <path d="M12 10 l4 0 l2 5 l-2.5 2 a12 12 0 0 0 5.5 5.5 l2 -2.5 l5 2 l0 4 a2 2 0 0 1 -2 2 a17 17 0 0 1 -16 -16 a2 2 0 0 1 2 -2z" fill="var(--orange)"/>
    </svg>
    <span class="phone-number">0412555018</span>
  </div>

  <p class="email">
    <svg width="28" height="20" viewBox="0 0 28 20" aria-hidden="true">
      <rect x="1.5" y="1.5" width="25" height="17" fill="none" stroke="var(--ink)" stroke-width="2.5"/>
      <path d="M2 2 L14 12 L26 2 M2 18 L11 10 M26 18 L17 10" fill="none" stroke="var(--ink)" stroke-width="2"/>
    </svg>
    melissadorne@mailbox.com
  </p>
</main>
</body>
</html>
```